Global Consulting firm needs a Business Card Design (Contest)

We need a business card design for a company with global reach called 'Hollowbrook Group'. Hollowbrook Group is a Trusted Procurement Advisor that consults for Pinnacle 400 and Meridel 900 companies to find cost reductions in their spending. We would like to see designs that communicate fiduciary trust and sense of partnership. The Front should have our logo w/ 'trusted procurement advisor', Employee name and title, company address, email, phone and fax (logo attached "Hollowbrook group final"). The color scheme and basic concept should be consistent with our presentation front page (attached "HBG presentation cover page"). The Back should have our website (www.hwbrookllc.com) and an array of our areas of expertise: office supplies, lab supplies, wireless telecom, MRO and IT (see "lab supplies" file for example).

```html
<!DOCTYPE html>
<html lang="en">
<head>
<meta charset="utf-8">
<title>Hollowbrook Group – Business Card</title>
<link rel="stylesheet" href="https://fonts.googleapis.com/css2?family=Crimson+Text:ital,wght@0,600;1,400&family=Source+Sans+3:wght@400;600;700&display=swap">
<style>
  :root {
    --page: #ecebe8;
    --card: #ffffff;
    --ink: #1c1c1c;
    --gold: #c8961e;
    --map: #efe6d2;
    --grey: #6d6d6d;
    --line: #c9c9c9;
    --navy: #1f2f6b;
    --serif: "Crimson Text", Georgia, serif;
    --sans: "Source Sans 3", Arial, sans-serif;
  }
  * { box-sizing: border-box; margin: 0; padding: 0; }
  html, body { width: 1200px; height: 1000px; overflow: hidden; }
  body { background: var(--page); position: relative; font-family: var(--sans); color: var(--ink); }

  .card {
    position: absolute; left: 265px; width: 665px; height: 397px;
    background: var(--card); border-radius: 22px; overflow: hidden;
    box-shadow: 0 6px 18px rgba(0,0,0,.12);
  }
  .card--front { top: 73px; }
  .card--back { top: 533px; }

  .world-map {
    position: absolute; border-radius: 40% 45% 35% 50%;
    background: radial-gradient(ellipse at center, var(--map) 0%, rgba(239,230,210,.55) 55%, rgba(239,230,210,0) 75%);
  }
  .card--front .world-map { left: 30px; top: 20px; width: 620px; height: 330px; }
  .card--back .world-map { left: 70px; top: 20px; width: 560px; height: 330px; }

  .brand { position: absolute; display: flex; align-items: center; }
  .brand__mark { width: 40px; height: 40px; border-radius: 50%; background: var(--gold); flex: none; }
  .brand__name { font-family: var(--serif); font-weight: 600; color: var(--ink); white-space: nowrap; }

  .card--front .brand { left: 32px; top: 36px; }
  .card--front .brand__name { font-size: 36px; margin-left: 18px; line-height: 1; }
  .tagline {
    position: absolute; left: 127px; top: 78px;
    font-family: var(--serif); font-style: italic; font-size: 19px; color: var(--ink);
  }

  .pyramid { position: absolute; left: 250px; top: 110px; }
  .pyramid__label { font-family: var(--sans); font-size: 9px; fill: var(--grey); }

  .person { position: absolute; left: 33px; top: 219px; }
  .person__name { font-size: 22px; font-weight: 700; color: var(--gold); line-height: 1.1; }
  .person__title { font-size: 19px; color: var(--ink); line-height: 1.2; }

  .rule { position: absolute; left: 33px; right: 32px; top: 276px; height: 2px; background: var(--gold); }

  .contacts { position: absolute; left: 33px; top: 287px; list-style: none; }
  .contacts li { display: flex; align-items: center; height: 27px; font-size: 19px; }
  .contacts svg { width: 22px; height: 22px; margin-right: 6px; flex: none; }

  .office { position: absolute; right: 32px; top: 290px; text-align: right; }
  .office__company { font-size: 18px; font-weight: 700; color: var(--gold); letter-spacing: .2px; }
  .office__city { font-size: 18px; margin-top: 2px; }

  .card--back .brand { left: 150px; top: 108px; }
  .card--back .brand__name { font-size: 32px; margin-left: 16px; line-height: 1; }
  .website {
    position: absolute; left: 0; right: 0; top: 150px; text-align: center;
    font-family: var(--serif); font-weight: 600; font-size: 18px; letter-spacing: 3.2px; color: var(--gold);
  }

  .expertise { position: absolute; left: 46px; top: 212px; display: flex; gap: 14px; list-style: none; }
  .expertise__item {
    position: relative; width: 104px; height: 72px;
    border: 1.5px solid var(--navy); background: #fff;
  }
  .expertise__label {
    position: absolute; left: 4px; top: -9px; height: 15px; padding: 0 10px 0 6px;
    background: var(--navy); color: #fff; font-size: 9.5px; font-weight: 600; line-height: 15px;
    border-radius: 2px 8px 0 0; white-space: nowrap;
  }
  .expertise__photo { position: absolute; left: 2px; right: 2px; top: 8px; bottom: 2px; }
  .photo--office { background: linear-gradient(135deg, #f5e36a, #f38fb5 55%, #9fd7f0); }
  .photo--lab { background: linear-gradient(135deg, #eef2f6, #c6d6e6 60%, #8fb0d0); }
  .photo--telecom { background: linear-gradient(135deg, #1a56a8, #4f8fd6 60%, #d9e6f3); }
  .photo--mro { background: linear-gradient(135deg, #ffffff, #d4d7db 60%, #9da3aa); }
  .photo--shipping { background: linear-gradient(135deg, #c99a63, #a8784a 60%, #7c5a38); }
</style>
</head>
<body>

<section class="card card--front" aria-label="Business card front">
  <div class="world-map" role="img" aria-label="Faint world map in the background"></div>

  <div class="brand">
    <span class="brand__mark"></span>
    <span class="brand__name">Hollowbrook Group</span>
  </div>
  <p class="tagline">Trusted Procurement Advisor</p>

  <svg class="pyramid" width="390" height="160" viewBox="0 0 390 160" aria-label="Procurement maturity pyramid">
    <g stroke="var(--line)" stroke-width="2">
      <line x1="97" y1="45" x2="270" y2="45"/>
      <line x1="97" y1="62" x2="270" y2="62"/>
      <line x1="97" y1="80" x2="270" y2="80"/>
      <line x1="97" y1="98" x2="270" y2="98"/>
      <line x1="97" y1="116" x2="270" y2="116"/>
    </g>
    <g text-anchor="end" class="pyramid__label">
      <text x="92" y="48">Best In Class</text>
      <text x="92" y="65">Technology</text>
      <text x="92" y="83">Process</text>
      <text x="92" y="101">Expertise/Market Intel</text>
      <text x="92" y="119">Category</text>
    </g>
    <g stroke="#fff" stroke-width="1.2">
      <polygon points="282,7 316,57 248,57" fill="#4a4a4a"/>
      <polygon points="248,57 316,57 328.5,75 235.5,75" fill="#3a3a3a"/>
      <polygon points="235.5,75 328.5,75 340,92 224,92" fill="#2f2f2f"/>
      <polygon points="224,92 340,92 352.5,110 211.5,110" fill="#8a8a8a"/>
      <polygon points="211.5,110 352.5,110 365,128 199,128" fill="#3a3a3a"/>
      <polygon points="199,128 365,128 373,140 191,140" fill="#2f2f2f"/>
    </g>
    <polygon points="191,140 373,140 378,150 186,150" fill="#1f1f1f"/>
  </svg>

  <div class="person">
    <p class="person__name">Daniel Okafor</p>
    <p class="person__title">Manager</p>
  </div>

  <div class="rule"></div>

  <ul class="contacts">
    <li>
      <svg viewBox="0 0 22 22" aria-label="Phone"><circle cx="11" cy="11" r="10" fill="none" stroke="var(--gold)" stroke-width="1.6"/><path d="M6 9c0-2 2-3 5-3s5 1 5 3l-2 1-1-2h-4l-1 2zM7 12h8v4H7z" fill="var(--gold)"/></svg>
      866 - 555 - 0142
    </li>
    <li>
      <svg viewBox="0 0 22 22" aria-label="Fax"><circle cx="11" cy="11" r="10" fill="none" stroke="var(--gold)" stroke-width="1.6"/><path d="M7 5h8v4H7zM5 9h12v6H5zM7 13h8v4H7z" fill="var(--gold)"/></svg>
      609 - 555 - 0187
    </li>
    <li>
      <svg viewBox="0 0 22 22" aria-label="Email"><circle cx="11" cy="11" r="10" fill="none" stroke="var(--gold)" stroke-width="1.6"/><rect x="5.5" y="7" width="11" height="8" fill="var(--gold)"/><path d="M5.5 7l5.5 4.5L16.5 7" fill="none" stroke="#fff" stroke-width="1"/></svg>
      info@hwbrookllc.com
    </li>
  </ul>

  <div class="office">
    <p class="office__company">HOLLOWBROOK GROUP</p>
    <p class="office__city">Ashford Ridge, New Jersey</p>
  </div>
</section>

<section class="card card--back" aria-label="Business card back">
  <div class="world-map" role="img" aria-label="Faint world map in the background"></div>

  <div class="brand">
    <span class="brand__mark"></span>
    <span class="brand__name">Hollowbrook Group</span>
  </div>
  <p class="website">www.hwbrookllc.com</p>

  <ul class="expertise">
    <li class="expertise__item"><span class="expertise__photo photo--office" role="img" aria-label="Photo of colourful sticky notes, pens and paper clips"></span><span class="expertise__label">Office Supplies</span></li>
    <li class="expertise__item"><span class="expertise__photo photo--lab" role="img" aria-label="Photo of laboratory test tubes and glassware"></span><span class="expertise__label">Lab Supplies</span></li>
    <li class="expertise__item"><span class="expertise__photo photo--telecom" role="img" aria-label="Photo of a hand holding a mobile phone before a globe"></span><span class="expertise__label">Wireless Telecom</span></li>
    <li class="expertise__item"><span class="expertise__photo photo--mro" role="img" aria-label="Photo of a wrench on a bolt"></span><span class="expertise__label">MRO</span></li>
    <li class="expertise__item"><span class="expertise__photo photo--shipping" role="img" aria-label="Photo of a handheld scanner over a shipping box"></span><span class="expertise__label">Shipping/Postage</span></li>
  </ul>
</section>

</body>
</html>
```